Business Card for Bright Furrow Lawn & Landscape

Double Sided Card Design - I think one side of the card should be cleaner, with logo, contact info, and "Complete Residential & Commercial Landscape Services", and on the other side it should list the services we offer:

- Lawn Care & Mowing
- Hedge & Shrub Trimming
- Leaf Removal & Clean Up
- Aeration & Sod
- Mulch & Rock Installations
- Landscape Installations & Renovations
- Commercial Snow Removal

Please make it clean and very professional... don't want it too be too busy, but want to tell them what we do.

Target Market(s)

Residential and Commercial

Industry/Entity Type

Landscape

Contact Information for Business Card

Fully Insured
Dale Ostrov
410-372-6184
Dostrov07@quillpost.net

Requirements
Must have
• Double Sided, Cleaner on one side, more information and text on the other side.

```html
<!DOCTYPE html>
<html lang="en">
<head>
<meta charset="utf-8">
<title>Bright Furrow Lawn &amp; Landscape – Business Card</title>
<link rel="stylesheet" href="https://fonts.googleapis.com/css2?family=Cinzel:wght@600&family=Roboto:wght@400;500&display=swap">
<style>
  :root {
    --backdrop: #1e1e1e;
    --card-black: #000000;
    --band-black: #141414;
    --leaf-green: #8cb400;
    --ink-white: #ffffff;
    --ink-black: #000000;
  }
  * { margin: 0; padding: 0; box-sizing: border-box; }
  html, body {
    width: 1200px; height: 960px; overflow: hidden;
    background: var(--backdrop);
  }
  .canvas { position: relative; width: 1200px; height: 960px; }

  .card {
    position: absolute; width: 600px; height: 342px; overflow: hidden;
    box-shadow: 0 4px 14px rgba(0,0,0,.5);
  }

  /* Front side */
  .card-front { left: 302px; top: 129px; background: var(--card-black); }
  .front-mark {
    position: absolute; left: 14px; top: 15px; width: 312px; height: 312px;
    border-radius: 50%; background: var(--leaf-green);
  }
  .front-brand {
    position: absolute; right: 36px; top: 42px; text-align: right;
    font-family: "Cinzel", serif; font-weight: 600; color: var(--leaf-green);
    line-height: 1;
  }
  .front-brand .brand-name { display: block; font-size: 28px; }
  .front-brand .brand-trade { display: block; font-size: 13.5px; letter-spacing: 2.6px; margin-top: 4px; }
  .holder-name {
    position: absolute; right: 36px; top: 150px;
    font-family: "Cinzel", serif; font-weight: 600; font-size: 25px;
    letter-spacing: 1px; color: var(--leaf-green);
  }
  .edge-tab {
    position: absolute; right: -22px; top: 141px; width: 44px; height: 44px;
    border-radius: 50%; background: var(--leaf-green);
  }
  .contact-list {
    position: absolute; right: 36px; top: 190px; list-style: none; text-align: right;
    font-family: "Roboto", sans-serif; font-size: 15px; color: var(--ink-white); line-height: 21px;
  }
  .contact-list li { display: flex; justify-content: flex-end; align-items: center; gap: 6px; }
  .contact-list svg { display: block; }
  .services-line {
    position: absolute; right: 36px; top: 243px; text-align: right;
    font-family: "Roboto", sans-serif; font-size: 16px; line-height: 20px; color: var(--ink-white);
  }
  .insured {
    position: absolute; right: 36px; top: 287px;
    font-family: "Cinzel", serif; font-weight: 600; font-size: 13px;
    letter-spacing: .6px; color: var(--leaf-green);
  }

  /* Back side */
  .card-back { left: 299px; top: 488px; background: var(--leaf-green); }
  .back-mark {
    position: absolute; left: 252px; top: 62px; width: 94px; height: 94px;
    border-radius: 50%; background: var(--ink-black);
  }
  .back-brand {
    position: absolute; left: 0; right: 0; top: 166px; text-align: center;
    font-family: "Cinzel", serif; font-weight: 600; color: var(--ink-black); line-height: 1;
  }
  .back-brand .brand-name { display: block; font-size: 30px; }
  .back-brand .brand-trade { display: block; font-size: 14px; letter-spacing: 3px; margin-top: 4px; }
  .service-list {
    position: absolute; left: 0; right: 0; top: 231px; text-align: center;
    font-family: "Roboto", sans-serif; font-size: 14.5px; line-height: 19px; color: var(--ink-black);
  }
  .service-list .dot { display: inline-block; width: 6px; height: 6px; border-radius: 50%;
    background: var(--ink-black); vertical-align: middle; margin: 0 4px; }
  .web-band {
    position: absolute; left: 0; right: 0; top: 300px; height: 27px;
    background: var(--band-black); text-align: center;
    font-family: "Roboto", sans-serif; font-weight: 500; font-size: 15px;
    letter-spacing: 1.4px; line-height: 27px; color: var(--leaf-green);
  }
</style>
</head>
<body>
<main class="canvas">

  <section class="card card-front" aria-label="Card front">
    <div class="front-mark" aria-hidden="true"></div>
    <h1 class="front-brand">
      <span class="brand-name">Bright Furrow</span>
      <span class="brand-trade">LAWN &amp; LANDSCAPE</span>
    </h1>
    <div class="edge-tab" aria-hidden="true"></div>
    <p class="holder-name">DALE OSTROV</p>
    <ul class="contact-list">
      <li>410-372-6184
        <svg width="9" height="13" viewBox="0 0 9 13" aria-hidden="true"><rect x="0.75" y="0.75" width="7.5" height="11.5" rx="1.3" fill="none" stroke="var(--leaf-green)" stroke-width="1.5"/><rect x="3" y="10" width="3" height="1" fill="var(--leaf-green)"/></svg>
      </li>
      <li>Dale@BrightFurrowMD.com
        <svg width="12" height="9" viewBox="0 0 12 9" aria-hidden="true"><rect width="12" height="9" fill="var(--leaf-green)"/><path d="M0 0 L6 5 L12 0" fill="none" stroke="var(--card-black)" stroke-width="1"/></svg>
      </li>
    </ul>
    <p class="services-line">Complete Residential &amp;<br>Commercial Landscape Services</p>
    <p class="insured">FULLY INSURED</p>
  </section>

  <section class="card card-back" aria-label="Card back">
    <div class="back-mark" aria-hidden="true"></div>
    <h2 class="back-brand">
      <span class="brand-name">Bright Furrow</span>
      <span class="brand-trade">LAWN &amp; LANDSCAPE</span>
    </h2>
    <p class="service-list">
      Lawn Care &amp; Mowing<span class="dot"></span>Hedge &amp; Shrub Trimming<br>
      Leaf Removal &amp; Clean Up<span class="dot"></span>Aeration &amp; Sod<span class="dot"></span>Mulch &amp; Rock Installations<br>
      Landscape Installations &amp; Renovations<span class="dot"></span>Commercial Snow Removal
    </p>
    <p class="web-band">www.BrightFurrowMD.com</p>
  </section>

</main>
</body>
</html>
```